Modern Business Card for Industrial Company

We need business cards updated with modern fonts and make it look more technical, sharp and clean. The logo should not be changed, but we are looking for fresh solutions for how other information on the card is laid out in an interesting way. The company provides machinery and services to the ceramic industry and deals with cutting-edge technology. The design should reflect a technologically advanced and modern company that deals with the latest European technologies.

Font styles to use
Sans Serif

Requirements
Must have
• Modern fonts, technical look and feel

```html
<!DOCTYPE html>
<html lang="en">
<head>
<meta charset="utf-8">
<title>Kelvaro Service – Business Card</title>
<link rel="stylesheet" href="https://fonts.googleapis.com/css2?family=Montserrat:wght@400;500;700;800&display=swap">
<style>
  :root {
    --brand-blue: #0a5a94;
    --brand-blue-dark: #074a7c;
    --brand-red: #b3202a;
    --steel-grey: #8c9095;
    --ink: #2b2d30;
    --paper: #ffffff;
    --paper-shade: #eef0f2;
    --backdrop: #c9c9c9;
  }
  * { box-sizing: border-box; margin: 0; padding: 0; }
  html, body {
    width: 1200px; height: 900px; overflow: hidden;
    background: var(--backdrop);
    font-family: "Montserrat", Arial, sans-serif;
  }
  .canvas { position: relative; width: 1200px; height: 900px; }

  .card {
    position: absolute; width: 700px; height: 400px; left: 250px;
    box-shadow: 0 6px 18px rgba(0,0,0,0.18);
    overflow: hidden;
  }

  /* Back side */
  .card--back { top: 30px; background: var(--brand-blue); }
  .back-brand {
    position: absolute; left: 0; right: 0; top: 135px;
    display: flex; align-items: center; justify-content: center; gap: 16px;
  }
  .back-brand__mark { width: 18px; height: 18px; background: var(--brand-red); }
  .back-brand__name {
    color: var(--paper); font-weight: 800; font-size: 54px; letter-spacing: 3px;
  }
  .back-web {
    position: absolute; left: 0; right: 0; top: 290px; text-align: center;
    color: var(--paper); font-weight: 700; font-size: 19px; letter-spacing: 1px;
  }

  /* Front side */
  .card--front {
    top: 470px;
    background: linear-gradient(120deg, var(--paper) 0%, var(--paper-shade) 55%, var(--paper) 100%);
  }
  .front-brand {
    position: absolute; left: 92px; top: 52px;
    color: var(--brand-blue); font-weight: 800; font-size: 46px; letter-spacing: 2px;
  }
  .side-band { position: absolute; left: 0; top: 0; width: 60px; height: 400px; }

  .contact {
    position: absolute; left: 92px; top: 196px;
    color: var(--ink); font-size: 18px; font-weight: 400; line-height: 1.3;
  }
  .contact__address { margin-bottom: 14px; }

  .person {
    position: absolute; right: 62px; top: 112px; text-align: right;
  }
  .person__name {
    color: var(--brand-blue); font-weight: 800; font-size: 27px; letter-spacing: 0.5px;
  }
  .person__role { color: var(--ink); font-size: 19px; font-weight: 500; margin-top: 2px; }
</style>
</head>
<body>
<main class="canvas">

  <section class="card card--back" aria-label="Card back">
    <div class="back-brand">
      <span class="back-brand__mark"></span>
      <span class="back-brand__name">KELVARO SERVICE</span>
    </div>
    <p class="back-web">www.kelvaro.com</p>
  </section>

  <section class="card card--front" aria-label="Card front">
    <p class="front-brand">KELVARO SERVICE</p>

    <svg class="side-band" viewBox="0 0 60 400" aria-hidden="true">
      <polygon points="0,150 48,165 48,190 0,175" fill="var(--brand-red)"/>
      <polygon points="0,179 48,194 48,200 0,185" fill="var(--paper)"/>
      <polygon points="0,189 48,204 48,372 0,396" fill="var(--brand-blue)"/>
      <!-- pin -->
      <g fill="none" stroke="var(--paper)" stroke-width="2">
        <path d="M24 232 c-6 0 -9 4 -9 8 c0 5 9 13 9 13 s9 -8 9 -13 c0 -4 -3 -8 -9 -8z"/>
        <circle cx="24" cy="240" r="2.5"/>
      </g>
      <!-- phone -->
      <path d="M16 290 c2 7 7 12 14 14 l3 -4 l-5 -3 l-2 2 c-3 -1 -5 -3 -6 -6 l2 -2 l-3 -5z" fill="var(--paper)"/>
      <!-- mail -->
      <g fill="none" stroke="var(--paper)" stroke-width="2">
        <rect x="13" y="320" width="22" height="15"/>
        <path d="M13 320 l11 9 l11 -9"/>
      </g>
      <!-- globe -->
      <g fill="none" stroke="var(--paper)" stroke-width="1.8">
        <circle cx="24" cy="358" r="10"/>
        <ellipse cx="24" cy="358" rx="4.5" ry="10"/>
        <path d="M14 358 h20 M16 352 h16 M16 364 h16"/>
      </g>
    </svg>

    <div class="contact">
      <p class="contact__address">418 Kepler Avenue, Suite 200<br>Dunmore, GA 30110</p>
      <p>555-014-2276</p>
      <p>mferrando@kelvaro.com</p>
      <p>www.kelvaro.com</p>
    </div>

    <div class="person">
      <p class="person__name">MARCO FERRANDO</p>
      <p class="person__role">President</p>
    </div>
  </section>

</main>
</body>
</html>
```